K&R Security Services PTY. LTD.

Ive just had my logo made and I'm looking for some simple but strong designs for my business cards the company is a security company.

Please use dark colors.

Regards,

Owen Deloit

Reason: Need more time for discussion with other directors

Industry/Entity Type

Security

Font styles to use
Sans Serif
Decorative

```html
<!DOCTYPE html>
<html lang="en">
<head>
<meta charset="utf-8">
<title>K&amp;R Security Services – Business Card</title>
<link rel="stylesheet" href="https://fonts.googleapis.com/css2?family=Oswald:wght@400;500;700&display=swap">
<style>
  :root {
    --page-bg: #2a2724;
    --card-black: #0a0a0a;
    --gloss-mid: #6e6e6e;
    --gloss-light: #d4d4d4;
    --frame-white: #f4f4f4;
    --name-grey: #8c8c8c;
    --text-white: #ffffff;
  }
  * { box-sizing: border-box; margin: 0; padding: 0; }
  html, body { width: 1200px; height: 900px; overflow: hidden; }
  body {
    background: var(--page-bg);
    font-family: "Oswald", "Arial Narrow", sans-serif;
    position: relative;
  }
  .card {
    position: absolute;
    width: 540px;
    height: 320px;
    border-radius: 26px;
    background:
      linear-gradient(118deg, var(--card-black) 0 44%, var(--gloss-mid) 44%, #9a9a9a 62%, var(--gloss-light) 100%);
    box-shadow: 0 18px 40px rgba(0,0,0,.55);
    overflow: hidden;
  }
  .card::after {
    content: "";
    position: absolute;
    inset: 12px;
    border: 5px solid var(--frame-white);
    border-radius: 20px;
    pointer-events: none;
  }
  .card--front { left: 80px; top: 120px; }
  .card--back  { left: 580px; top: 460px; }

  .company-name {
    position: absolute;
    color: var(--text-white);
    font-weight: 500;
    text-transform: uppercase;
    letter-spacing: 1.5px;
    text-align: center;
    line-height: 1.3;
  }
  .card--front .company-name {
    left: 90px; right: 90px; top: 128px;
    font-size: 24px;
  }
  .card--back .company-name {
    left: 34px; top: 118px; width: 180px;
    font-size: 14px;
  }

  .holder-name {
    position: absolute;
    left: 238px; top: 34px;
    font-size: 36px;
    font-weight: 700;
    color: var(--name-grey);
    letter-spacing: 1px;
    text-transform: uppercase;
    text-shadow: 0 1px 0 rgba(255,255,255,.35), 0 -1px 0 rgba(0,0,0,.4);
  }
  .contact-list {
    position: absolute;
    left: 308px; top: 92px;
    list-style: none;
  }
  .contact-list li {
    display: flex;
    align-items: center;
    gap: 8px;
    height: 26px;
    font-size: 16px;
    color: var(--text-white);
    letter-spacing: .5px;
    text-transform: uppercase;
  }
  .icon { width: 20px; height: 20px; flex: none; }
  .postal-address {
    position: absolute;
    left: 34px; top: 252px;
    display: flex;
    align-items: center;
    gap: 10px;
    font-size: 21px;
    font-weight: 500;
    color: var(--text-white);
    letter-spacing: 1px;
    text-transform: uppercase;
  }
  .postal-address .icon { width: 28px; height: 28px; }
</style>
</head>
<body>

<section class="card card--front" aria-label="Card front">
  <p class="company-name">K&amp;R Security Services PTY. LTD.</p>
</section>

<section class="card card--back" aria-label="Card back">
  <p class="company-name">K&amp;R Security Services PTY. LTD.</p>

  <h1 class="holder-name">Owen Deloit</h1>

  <ul class="contact-list">
    <li>
      <svg class="icon" viewBox="0 0 20 20" aria-hidden="true"><circle cx="10" cy="10" r="10" fill="#fff"/><path d="M6.5 5.5l2 .2.6 2.3-1.2.9a6 6 0 0 0 3.2 3.2l.9-1.2 2.3.6.2 2a1.3 1.3 0 0 1-1.4 1.1A8.6 8.6 0 0 1 5.4 6.9a1.3 1.3 0 0 1 1.1-1.4z" fill="#111"/></svg>
      0400 318 276
    </li>
    <li>
      <svg class="icon" viewBox="0 0 20 20" aria-hidden="true"><circle cx="10" cy="10" r="10" fill="#fff"/><rect x="6" y="5" width="8" height="10" rx="1" fill="none" stroke="#111" stroke-width="1.6"/><line x1="8" y1="12.5" x2="12" y2="12.5" stroke="#111" stroke-width="1.4"/></svg>
      (03) 9012 4410
    </li>
    <li>
      <svg class="icon" viewBox="0 0 20 20" aria-hidden="true"><circle cx="10" cy="10" r="10" fill="#fff"/><rect x="5" y="6.5" width="10" height="7" fill="none" stroke="#111" stroke-width="1.4"/><path d="M5 6.5l5 4 5-4" fill="none" stroke="#111" stroke-width="1.4"/></svg>
      owen@deloitsec.net.au
    </li>
    <li>
      <svg class="icon" viewBox="0 0 20 20" aria-hidden="true"><circle cx="10" cy="10" r="10" fill="#fff"/><rect x="5" y="6.5" width="10" height="7" fill="#111"/><path d="M5 6.5l5 4 5-4" fill="none" stroke="#fff" stroke-width="1.2"/></svg>
      kr@deloitsec.net.au
    </li>
  </ul>

  <p class="postal-address">
    <svg class="icon" viewBox="0 0 28 28" aria-hidden="true"><circle cx="14" cy="14" r="14" fill="#fff"/><path d="M7 14l7-6 7 6h-2v6h-3.5v-4h-3v4H9v-6z" fill="#111"/></svg>
    P.O. Box 14 Elmwood Victoria 3188
  </p>
</section>

</body>
</html>
```